Flyer Template Design

I have attached 4 files. I would like a design template that could be used across these documents so that they have a common look and feel. The content of the documents is tested and should not be changed significantly. The images can be changed. I have also attache our logo for color compatibility.
Updates

Need extra days to review

Target Market(s)

Wealthy Christian donors

Font styles to use
Serif
Sans Serif

```html
<!DOCTYPE html>
<html lang="en">
<head>
<meta charset="utf-8">
<title>Fishing the Great Commission</title>
<link href="https://fonts.googleapis.com/css2?family=Montserrat:ital,wght@0,600;0,800;0,900;1,700&family=Open+Sans:ital,wght@0,400;0,600;1,400;1,600&display=swap" rel="stylesheet">
<style>
  :root {
    --green: #3f8a2f;
    --green-light: #6db33f;
    --green-dark: #1f4f1d;
    --ink: #3a3a3a;
    --panel-text: #e8efe6;
    --paper: #ffffff;
  }
  * { box-sizing: border-box; margin: 0; padding: 0; }
  html, body { width: 889px; height: 1200px; overflow: hidden; background: var(--paper); }
  body { font-family: "Open Sans", Arial, sans-serif; color: var(--ink); }
  .flyer { position: relative; width: 889px; height: 1200px; overflow: hidden; }

  .hero-art { position: absolute; top: 0; right: 0; width: 460px; height: 360px; }

  .title {
    position: absolute; left: 40px; top: 22px;
    font-family: "Montserrat", Arial, sans-serif; font-weight: 900;
    color: var(--green-dark); line-height: .95; letter-spacing: -1px;
  }
  .title .line-1 { display: block; font-size: 68px; }
  .title .line-2 { display: block; font-size: 42px; }
  .title .accent { color: var(--green-light); }
  .title .line-3 { display: block; font-size: 48px; margin-top: 2px; }

  .intro {
    position: absolute; left: 40px; top: 196px; width: 430px;
    font-size: 15px; line-height: 22px;
  }

  .section-heading {
    font-family: "Montserrat", Arial, sans-serif; font-weight: 800;
    color: var(--green-light); font-size: 28px; letter-spacing: .3px; text-transform: uppercase;
    line-height: 1.1;
  }
  .section-heading .strong { color: var(--green-dark); }

  .nations { position: absolute; left: 40px; top: 376px; width: 810px; }
  .nations p { margin-top: 8px; font-size: 15px; line-height: 22px; }

  .stand { position: absolute; left: 40px; top: 552px; width: 385px; }
  .stand p { margin-top: 10px; font-size: 15px; line-height: 22px; }
  .stand-photo { position: absolute; left: 40px; top: 832px; width: 230px; height: 145px;
    background: linear-gradient(135deg, #b89a7a, #6e5a48 60%, #3d352e); }
  .stand-note { position: absolute; left: 40px; top: 988px; width: 400px;
    font-style: italic; font-size: 14px; color: var(--ink); }
  .stand-note strong { display: block; font-family: "Montserrat", Arial, sans-serif;
    font-size: 20px; color: var(--green); font-weight: 700; margin-top: 2px; }

  .brand { position: absolute; left: 40px; top: 1070px; display: flex; align-items: center; gap: 10px;
    font-family: "Montserrat", Arial, sans-serif; font-weight: 800; font-size: 16px;
    color: var(--green-dark); text-transform: uppercase; line-height: 1.1; }
  .brand .mark { width: 34px; height: 34px; border-radius: 50%; background: var(--green); }

  .hastening { position: absolute; left: 444px; top: 544px; width: 445px; bottom: 42px;
    background: var(--green-dark); color: #fff; padding: 18px 32px 0 40px; }
  .hastening .section-heading { color: #fff; font-size: 36px; line-height: 1.02; }
  .hastening p { margin-top: 12px; font-size: 14px; line-height: 21px; color: var(--panel-text); }
  .hastening .call { margin-top: 18px; font-family: "Montserrat", Arial, sans-serif;
    font-style: italic; font-weight: 700; font-size: 17px; line-height: 23px; color: #fff; text-align: center; }

  .footer { position: absolute; left: 355px; right: 0; top: 1158px; height: 42px;
    background: var(--green); color: #fff; font-size: 13px;
    display: flex; align-items: center; justify-content: flex-end; padding-right: 40px; }
  .footer strong { font-weight: 600; margin-left: 4px; }
</style>
</head>
<body>
<div class="flyer">

  <svg class="hero-art" viewBox="0 0 460 360">
    <polygon points="0,0 460,0 460,40 180,0" fill="#1f4f1d"/>
    <polygon points="120,120 240,0 360,120 240,240" fill="#3f8a2f"/>
    <g role="img" aria-label="Portrait photo of an elderly man from an unreached people group">
      <polygon points="250,10 350,110 250,210 150,110" fill="#9c7a5c"/>
    </g>
    <g role="img" aria-label="Portrait photo of a man wearing a turban">
      <polygon points="360,0 460,0 460,200 360,100" fill="#7a6452"/>
    </g>
    <g role="img" aria-label="Portrait photo of a smiling woman in a red headscarf">
      <polygon points="260,230 360,130 460,230 360,330" fill="#b0463c"/>
    </g>
    <polygon points="150,250 240,340 150,430 60,340" fill="#6db33f" opacity=".85"/>
    <polygon points="360,330 460,230 460,360 380,360" fill="#1f4f1d"/>
  </svg>

  <h1 class="title">
    <span class="line-1">FISHING</span>
    <span class="line-2"><span class="accent">THE</span> GREAT</span>
    <span class="line-3">COMMISSION</span>
  </h1>

  <p class="intro">Before Jesus ascended into heaven, He commanded his apostles, “Go and make disciples of all nations.” For more than 2000 years the church has been working to fulfill this “Great Commission,” and much has been accomplished. But now, for the first time in history, our generation has the real opportunity to finish the Great Commission in our lifetimes.</p>

  <section class="nations">
    <h2 class="section-heading">It’s about nations</h2>
    <p>In the Bible, the word “nations” refers to people groups; groups of people who share a common ethnicity, culture, and language. So when Jesus said, “Go and make disciples if all nations,” He was telling us to take the gospel to every people group on earth. Amazingly, there are about 12,000 of these people groups scattered throughout the world. And the Great Commission to make disciples in every one of them.</p>
  </section>

  <section class="stand">
    <h2 class="section-heading"><span class="strong">Where</span> do we stand?</h2>
    <p>Today, there are still about 500 people groups who have never heard the gospel. Most of these groups are small and located in remote, difficult places. These remaining “unengaged” people groups have no known believers.</p>
    <p>But now that we know who and where these groups are, by God’s grace it is possible that we can engage every one of them with the gospel within the next 3 years.</p>
  </section>
  <div class="stand-photo" role="img" aria-label="Photo of a young woman and a bearded man from remote people groups"></div>
  <p class="stand-note">In other words, we can finish <strong>The Great Commission!</strong></p>

  <div class="brand"><span class="mark"></span><span>The Harvest<br>Fund</span></div>

  <section class="hastening">
    <h2 class="section-heading">Hastening<br>His coming</h2>
    <p>The Bible says that believers “ought to live holy and godly lives, looking for and hastening the coming of the day of God.” It also says that day will not come until the gospel has been preached to “all nations”. So how can hasten the day of his coming? By finishing the work he gave us to do, making disciples in all nations.</p>
    <p>Partner with the Harvest Fund and finance the missionaries who are taking the gospel for the first time to those last remaining people groups. Your investment will hasten the coming of the day of God” by accelerating the effort to make “disciples in every nation.” In 2016, our partners helped take the gospel to 231 people groups in 35 countries.</p>
    <p class="call">Join us as we invest to make disciples in “all nations” by 2022.</p>
  </section>

  <footer class="footer">To learn more, email Daniel Morrow at <strong>dmorrow@harvestfund.org</strong>.</footer>
</div>
</body>
</html>
```